KVRT CERTIFICATES

We would like to redesign our swimming certificates. These are the certificates we give out to children in our swimming program every time they go up a level.

I have attached a copy of our current certificate to give you a general idea of what the layout etc.

This would be a 2 sided A4 full colour certificate template that we then individually print a child’s name and assessment details on to and present to them when they are assessed to move up a level

We are currently preparing to rebrand a number of areas of our program and these certificates should work to match the branding we are moving to. To help with this I have attached a copy of the template for our new website which should be operational within the next 4 to 6 weeks.

We are also about to release a new logo and it is attached for your use.

These certificates should also incorporate our new mascots & sea characters.

The KVRT boy & girl mascot should be used on all certificates. I have attached images of them in various positions for general use.

In all there will be 5 different certificates to suit the 5 sea characters we have to denote the 5 different stages within our program. The certificates should be designed to suit the general age of the children in that program:

Starfish – Toddler Program – 4 months to 3 years
Seahorse – Water Confidence Program – 3 to 6 years
Turtle – Learn-to-swim Program – 5 to 8 years
Fish – High end Learn-to-swim Program – 6 to 9 years
Dolphin – Squad Program – 7 to 12 years

The back of all certificates will be the same.

I would like the certificates to be bright, colourful, fun & age appropriate. I feel our current certificates are to busy and dated.

Requirements
Must have
• White areas on the certificate so we can print the child's individual details onto the certificate.

'Teaching families to swim since 1994!'

Address & contact info as per our current certificate.

Website address & Pixmora logo.

'Congratulations' 'you have completed' Skills Achieved' as shown on our current certificate.

On the back of the certificate I would like to present and outline the KVRT boy & girl Mascots as well as the sea characters and link them to the program to which they represent.

```html
<!DOCTYPE html>
<html lang="en">
<head>
<meta charset="utf-8">
<title>KVRT Swimming Certificate – Front and Back</title>
<link href="https://fonts.googleapis.com/css2?family=Open+Sans:wght@400;600&family=Parisienne&display=swap" rel="stylesheet">
<style>
  :root {
    --stage-top: #ffffff;
    --stage-bottom: #2d8ff0;
    --card-edge: #1c2a8f;
    --ink: #222222;
    --script-ink: #1d1d1d;
    --field-line: #9a9a9a;
    --white: #ffffff;
    --brand-blue: #1d4fc4;
    --mascot-blue: #2f49d8;
    --mascot-red: #e32b2b;
    --star-pink: #f07ab8;
  }
  * { box-sizing: border-box; margin: 0; padding: 0; }
  html, body { width: 1200px; height: 900px; overflow: hidden; }
  body {
    background: linear-gradient(180deg, var(--stage-top) 0%, #e6f0fc 35%, var(--stage-bottom) 100%);
    font-family: "Open Sans", Arial, sans-serif;
    position: relative;
  }
  .certificate {
    position: absolute;
    top: 68px;
    width: 542px;
    height: 768px;
    background: var(--white);
    border: 1px solid var(--card-edge);
    box-shadow: 3px 4px 8px rgba(0,0,0,0.45);
    overflow: hidden;
  }
  .certificate--front { left: 34px; }
  .certificate--back { left: 618px; }
  .waves { position: absolute; inset: 0; width: 542px; height: 768px; }
  .brand {
    position: absolute;
    top: 24px;
    left: 0;
    width: 542px;
    display: flex;
    justify-content: center;
    align-items: center;
    gap: 8px;
    color: var(--brand-blue);
    font-weight: 600;
    font-size: 38px;
    line-height: 52px;
    letter-spacing: 1px;
  }
  .brand__dot { width: 16px; height: 16px; border-radius: 50%; background: var(--brand-blue); }
  .brand__sub {
    position: absolute;
    top: 82px; left: 0; width: 542px;
    text-align: center;
    color: var(--brand-blue);
    font-weight: 600;
    line-height: 12px;
  }
  .brand__sub-name { display: block; font-size: 11px; }
  .brand__sub-kind { display: block; font-size: 8.5px; letter-spacing: 1px; text-transform: uppercase; }
  .tagline { position: absolute; color: var(--ink); font-size: 24px; white-space: nowrap; }
  .tagline strong { font-weight: 600; }
  .certificate--front .tagline { top: 172px; left: 0; width: 542px; text-align: center; }
  .script {
    position: absolute; left: 0; width: 542px; text-align: center;
    font-family: "Parisienne", cursive; font-weight: 400; color: var(--script-ink);
  }
  .script--title { top: 254px; font-size: 40px; }
  .script--label { font-size: 24px; }
  .script--completed { top: 380px; }
  .script--skills { top: 538px; }
  .field { position: absolute; left: 126px; width: 296px; border: 1px solid var(--field-line); background: var(--white); }
  .field--name { top: 324px; height: 41px; }
  .field--level { top: 424px; height: 104px; }
  .illustration { position: absolute; border-radius: 40% 40% 20% 20%; }
  .mascot-boy { left: 2px; top: 486px; width: 120px; height: 168px; background: linear-gradient(180deg, var(--mascot-blue) 0 18%, #f6cfd2 18% 48%, var(--mascot-red) 48% 78%, #f6cfd2 78%); }
  .mascot-girl { left: 424px; top: 486px; width: 112px; height: 168px; background: linear-gradient(180deg, var(--mascot-blue) 0 18%, #f4c64a 18% 48%, var(--mascot-red) 48% 78%, #f6cfd2 78%); }
  .footer {
    position: absolute; top: 672px; left: 31px;
    display: grid; grid-template-columns: 201px 230px;
    color: var(--white); font-size: 10.5px; line-height: 12px;
  }
  .footer__site { font-style: normal; white-space: nowrap; }
  .footer__name { font-size: 11px; margin-bottom: 1px; }
  .social { position: absolute; top: 713px; right: 22px; display: flex; align-items: center; gap: 6px; color: var(--white); font-size: 11px; }
  .social__ring { width: 27px; height: 27px; border: 2px solid var(--white); border-radius: 50%; }
  .mascots-poolside { left: 342px; top: 17px; width: 196px; height: 180px; border-radius: 30px; background: linear-gradient(180deg, var(--mascot-blue) 0 20%, #f3c9a8 20% 50%, var(--mascot-red) 50% 75%, #bfe9f6 75%); }
  .starfish { left: -20px; top: 230px; width: 232px; height: 302px; border-radius: 48% 52% 40% 44%; background: radial-gradient(circle at 50% 50%, #f59ac8, var(--star-pink) 70%); }
  .certificate--back .tagline { top: 274px; left: 230px; font-size: 15.5px; }
  .program-note { position: absolute; top: 310px; left: 234px; width: 272px; font-size: 10.4px; line-height: 16.4px; color: var(--ink); }
</style>
</head>
<body>

<section class="certificate certificate--front" aria-label="Certificate front">
  <svg class="waves" viewBox="0 0 542 768" aria-hidden="true">
    <defs>
      <linearGradient id="skyFront" x1="0" y1="0" x2="0" y2="1">
        <stop offset="0" stop-color="#f7931e"/><stop offset="1" stop-color="#f0590f"/>
      </linearGradient>
      <radialGradient id="glowFront" cx="0.5" cy="0.4" r="0.5">
        <stop offset="0" stop-color="#fff6d9"/><stop offset="0.6" stop-color="#ffd27a" stop-opacity="0.6"/><stop offset="1" stop-color="#ffd27a" stop-opacity="0"/>
      </radialGradient>
      <linearGradient id="mintFront" x1="0" y1="0" x2="0" y2="1">
        <stop offset="0" stop-color="#c9f5de"/><stop offset="1" stop-color="#ffffff"/>
      </linearGradient>
      <linearGradient id="seaFront" x1="0" y1="0" x2="0" y2="1">
        <stop offset="0" stop-color="#5fd0e6"/><stop offset="1" stop-color="#2b8fbf"/>
      </linearGradient>
    </defs>
    <rect width="542" height="240" fill="url(#mintFront)"/>
    <path d="M0 0H542V130C470 150 420 110 330 120C250 130 200 160 120 145C70 136 30 128 0 140Z" fill="url(#skyFront)"/>
    <ellipse cx="271" cy="55" rx="170" ry="75" fill="url(#glowFront)"/>
    <path d="M0 640C90 600 170 610 260 625C350 640 450 615 542 600V768H0Z" fill="#f9b21c"/>
    <path d="M0 655C100 620 180 630 270 640C360 650 460 630 542 615V768H0Z" fill="url(#seaFront)"/>
  </svg>

  <div class="brand"><span class="brand__dot"></span>KVRT</div>
  <p class="brand__sub"><span class="brand__sub-name">Kestrel Vale</span><span class="brand__sub-kind">Swimming Academy</span></p>

  <p class="tagline">'Teaching families to <strong>swim</strong> since 1994!'</p>
  <h1 class="script script--title">Congratulations</h1>
  <div class="field field--name"></div>
  <p class="script script--label script--completed">you have completed</p>
  <div class="field field--level"></div>
  <p class="script script--label script--skills">Skills Achieved</p>

  <div class="illustration mascot-boy" role="img" aria-label="Boy mascot in graduation cap and red swimsuit giving thumbs up"></div>
  <div class="illustration mascot-girl" role="img" aria-label="Girl mascot in graduation cap and red swimsuit clapping"></div>

  <div class="footer">
    <address class="footer__site">
      <p class="footer__name">KVRT Marlowe Aquatic Centre</p>
      <p>14 Fenwick St</p><p>Brindlewood QLD 4870</p><p>Ph: 07 5550 1284</p><p>Fax: 07 5550 1290</p><p>E: admin@kvrtswim.com.au</p>
    </address>
    <address class="footer__site">
      <p class="footer__name">KVRT Harlow Heights Aquatic Centre</p>
      <p>Cnr North and Lindell Sts</p><p>Brindlewood QLD 4870</p><p>Ph: 07 5550 3362</p><p>Fax: 07 5550 1290</p><p>E: hhadmin@kvrtswim.com.au</p>
    </address>
  </div>
  <div class="social">Pixmora<span class="social__ring"></span></div>
</section>

<section class="certificate certificate--back" aria-label="Certificate back">
  <svg class="waves" viewBox="0 0 542 768" aria-hidden="true">
    <defs>
      <linearGradient id="skyBack" x1="0" y1="0" x2="0" y2="1">
        <stop offset="0" stop-color="#f7931e"/><stop offset="1" stop-color="#f0590f"/>
      </linearGradient>
      <radialGradient id="glowBack" cx="0.5" cy="0.4" r="0.5">
        <stop offset="0" stop-color="#fff6d9"/><stop offset="0.6" stop-color="#ffd27a" stop-opacity="0.6"/><stop offset="1" stop-color="#ffd27a" stop-opacity="0"/>
      </radialGradient>
      <linearGradient id="mintBack" x1="0" y1="0" x2="0" y2="1">
        <stop offset="0" stop-color="#c9f5de"/><stop offset="1" stop-color="#ffffff"/>
      </linearGradient>
      <linearGradient id="seaBack" x1="0" y1="0" x2="0" y2="1">
        <stop offset="0" stop-color="#5fd0e6"/><stop offset="1" stop-color="#2b8fbf"/>
      </linearGradient>
    </defs>
    <rect width="542" height="240" fill="url(#mintBack)"/>
    <path d="M0 0H542V130C470 150 420 110 330 120C250 130 200 160 120 145C70 136 30 128 0 140Z" fill="url(#skyBack)"/>
    <ellipse cx="271" cy="55" rx="170" ry="75" fill="url(#glowBack)"/>
    <path d="M0 640C90 600 170 610 260 625C350 640 450 615 542 600V768H0Z" fill="#f9b21c"/>
    <path d="M0 655C100 620 180 630 270 640C360 650 460 630 542 615V768H0Z" fill="url(#seaBack)"/>
  </svg>

  <div class="brand"><span class="brand__dot"></span>KVRT</div>
  <p class="brand__sub"><span class="brand__sub-name">Kestrel Vale</span><span class="brand__sub-kind">Swimming Academy</span></p>

  <div class="illustration mascots-poolside" role="img" aria-label="Boy and girl mascots in graduation caps sitting on the pool edge"></div>
  <div class="illustration starfish" role="img" aria-label="Smiling pink starfish sea character"></div>

  <p class="tagline">'Teaching families to <strong>swim</strong> since 1994!'</p>
  <div class="program-note">
    <p>The KVRT Level Progression provides each child with a gentle progression of skills from basic water confidence to swimming all four strokes.</p>
    <p>The progression has also been designed to suit the individual needs and ability level of each child, allowing them to progress at their own pace.</p>
    <p>On the front of this certificate is the level the swimmer has currently achieved as well as the skills they have achieved to an appropriate level. Regardless of the level reached by the swimmer in the KVRT Program, it is strongly recommended that children be appropriately attired and supervised at all times while in or around water.</p>
  </div>

  <div class="footer">
    <address class="footer__site">
      <p class="footer__name">KVRT Marlowe Aquatic Centre</p>
      <p>14 Fenwick St</p><p>Brindlewood QLD 4870</p><p>Ph: 07 5550 1284</p><p>Fax: 07 5550 1290</p><p>E: admin@kvrtswim.com.au</p>
    </address>
    <address class="footer__site">
      <p class="footer__name">KVRT Harlow Heights Aquatic Centre</p>
      <p>Cnr North and Lindell Sts</p><p>Brindlewood QLD 4870</p><p>Ph: 07 5550 3362</p><p>Fax: 07 5550 1290</p><p>E: hhadmin@kvrtswim.com.au</p>
    </address>
  </div>
  <div class="social">Pixmora<span class="social__ring"></span></div>
</section>

</body>
</html>
```